In need a simple business/calling card

I am looking for a VERY simple, professional, and classic business card which is really more of a calling card. In the Halvorsen & Pike or Whitlow kind of style. I am also open to a solid boarder but not necessary. I prefer no logos or "designs".

Target Market(s)

general

Contact Information for Business Card

Daniel Brenwick (or Daniel T. Brenwick)
+1 555 274 6180
dan@brenwick.example

Thats it!

Font styles to use
Serif
Sans Serif
Script

Colors

Designer to choose colors to be used in the design.

Requirements
Must have
• everything on the card details section.
Nice to have
• n/a
Should not have
• No logos.

```html
<!DOCTYPE html>
<html lang="en">
<head>
<meta charset="utf-8">
<title>Daniel T. Brenwick – Calling Card</title>
<link rel="stylesheet" href="https://fonts.googleapis.com/css2?family=Roboto+Condensed:wght@400;700&display=swap">
<style>
  :root {
    --backdrop: #2b1c14;
    --card: #ffffff;
    --ink: #1a1a1a;
    --muted: #8a8a8a;
    --stripe: #1a1a1a;
  }
  html, body {
    margin: 0;
    width: 1200px;
    height: 1200px;
    overflow: hidden;
    background: var(--backdrop);
  }
  .canvas {
    position: relative;
    width: 1200px;
    height: 1200px;
  }
  .card {
    position: absolute;
    left: 100px;
    top: 317px;
    width: 1000px;
    height: 566px;
    background: var(--card);
    box-shadow: 0 18px 40px rgba(0, 0, 0, 0.45);
  }
  .name-row {
    position: absolute;
    left: 0;
    right: 0;
    top: 172px;
    display: flex;
    align-items: center;
    gap: 14px;
  }
  .stripes {
    flex: 1;
    height: 65px;
    background: repeating-linear-gradient(
      to bottom,
      var(--stripe) 0 2.5px,
      transparent 2.5px 5px
    );
  }
  .name {
    position: relative;
    margin: 0;
    font-family: "Roboto Condensed", "Arial Narrow", sans-serif;
    font-weight: 700;
    font-size: 78px;
    line-height: 1;
    letter-spacing: -0.5px;
    color: var(--ink);
    white-space: nowrap;
  }
  .name-reflection {
    position: absolute;
    left: 0;
    top: 100%;
    margin-top: -14px;
    transform: scaleY(-1);
    color: var(--ink);
    opacity: 0.18;
    -webkit-mask-image: linear-gradient(to top, #000 0%, transparent 45%);
    mask-image: linear-gradient(to top, #000 0%, transparent 45%);
    pointer-events: none;
  }
  .contact {
    position: absolute;
    left: 0;
    right: 0;
    top: 372px;
    display: flex;
    justify-content: center;
    gap: 36px;
    font-family: "Roboto Condensed", "Arial Narrow", sans-serif;
    font-weight: 400;
    font-size: 28px;
    color: var(--muted);
  }
</style>
</head>
<body>
  <div class="canvas">
    <section class="card">
      <div class="name-row">
        <span class="stripes" aria-hidden="true"></span>
        <h1 class="name">Daniel T. Brenwick<span class="name-reflection" aria-hidden="true">Daniel T. Brenwick</span></h1>
        <span class="stripes" aria-hidden="true"></span>
      </div>
      <p class="contact">
        <span class="phone">+1 555 274 6180</span>
        <span class="email">dan@brenwick.example</span>
      </p>
    </section>
  </div>
</body>
</html>
```